Vardena General Painting Ltd. - Construction painting company providing high-quality service

We need a logo and business card design for a painting company that provides high-quality work for major developers and builders in Calgary, Alberta. Our projects include commercial high-rise residential towers. We would like designs that communicate professionalism and high quality service.
Updates
Need extra days to review
Target Market(s)
Developers and builders
Industry/Entity Type
Construction
Contact Information for Business Card
Company name, employee name, title, phone number, email address
Font styles to use
Colors
Designer to choose colors to be used in the design.
Look and feel
Each slider illustrates characteristics of the customer's brand and the style your logo design should communicate.

```html
<!DOCTYPE html>
<html lang="en">
<head>
<meta charset="utf-8">
<title>Vardena General Painting Ltd. — Business Card</title>
<link rel="stylesheet" href="https://fonts.googleapis.com/css2?family=Cinzel:wght@400&family=Open+Sans:wght@400&display=swap">
<style>
  :root {
    --backdrop: #2f2f2c;
    --card: #141414;
    --wordmark: #bdbdc2;
    --white: #ffffff;
    --green: #a6c34a;
    --orange: #e08a3c;
    --blue: #5e9fd1;
    --text-light: #d6d6d9;
  }
  * { margin: 0; padding: 0; box-sizing: border-box; }
  html, body { width: 1200px; height: 824px; overflow: hidden; }
  body {
    background: var(--backdrop);
    position: relative;
    font-family: "Open Sans", sans-serif;
  }
  .card {
    position: absolute;
    width: 520px;
    height: 300px;
    background: var(--card);
    border-radius: 4px;
    box-shadow: 0 10px 30px rgba(0,0,0,0.45);
  }
  .card--front { left: 60px; top: 70px; }
  .card--back { left: 620px; top: 300px; }

  .wordmark {
    font-family: "Cinzel", serif;
    font-weight: 400;
    color: var(--wordmark);
    line-height: 1;
  }
  .card--front .wordmark {
    position: absolute;
    right: 40px;
    bottom: 60px;
    text-align: right;
  }
  .card--front .wordmark__name { font-size: 58px; letter-spacing: 3px; display: block; }
  .card--front .wordmark__line { font-size: 13px; letter-spacing: 4px; display: block; margin-top: 8px; }

  .card--back .wordmark {
    position: absolute;
    left: 36px;
    top: 112px;
  }
  .card--back .wordmark__name { font-size: 30px; letter-spacing: 2px; display: block; }
  .card--back .wordmark__line { font-size: 7px; letter-spacing: 2px; display: block; margin-top: 5px; }

  .divider {
    position: absolute;
    left: 262px;
    top: 60px;
    width: 2px;
    height: 180px;
    background: linear-gradient(var(--blue) 0 33%, var(--green) 33% 66%, var(--orange) 66% 100%);
  }
  .contact {
    position: absolute;
    left: 290px;
    top: 82px;
  }
  .contact__name {
    font-family: "Cinzel", serif;
    font-size: 24px;
    color: var(--text-light);
    letter-spacing: 1px;
  }
  .contact__title {
    font-size: 14px;
    color: var(--green);
    margin-top: 2px;
    letter-spacing: 0.5px;
  }
  .contact__row {
    display: flex;
    align-items: center;
    gap: 8px;
    font-size: 14px;
    color: var(--text-light);
    margin-top: 10px;
  }
  .contact__row svg { width: 15px; height: 15px; flex: none; }

  .logo-lockup {
    position: absolute;
    left: 50px;
    top: 690px;
    color: var(--white);
  }
  .logo-lockup .wordmark { color: var(--white); }
  .logo-lockup .wordmark__name { font-size: 44px; letter-spacing: 3px; display: block; }
  .logo-lockup .wordmark__line { font-size: 10px; letter-spacing: 3px; display: block; margin-top: 6px; }
</style>
</head>
<body>

  <section class="card card--front" aria-label="Business card front">
    <div class="wordmark">
      <span class="wordmark__name">VARDENA</span>
      <span class="wordmark__line">GENERAL PAINTING LTD.</span>
    </div>
  </section>

  <section class="card card--back" aria-label="Business card back">
    <div class="wordmark">
      <span class="wordmark__name">VARDENA</span>
      <span class="wordmark__line">GENERAL PAINTING LTD.</span>
    </div>
    <div class="divider"></div>
    <div class="contact">
      <p class="contact__name">YOUR NAME</p>
      <p class="contact__title">JOB TITLE</p>
      <p class="contact__row">
        <svg viewBox="0 0 16 16" aria-hidden="true"><path fill="#a6c34a" d="M4 1l2.5 3-1.5 2c.8 1.8 2.2 3.2 4 4l2-1.5 3 2.5-1.5 2.5C7 14 2 9 1.5 2.5z"/></svg>
        000 000 0000
      </p>
      <p class="contact__row">
        <svg viewBox="0 0 16 16" aria-hidden="true"><rect x="1" y="3" width="14" height="10" fill="#a6c34a"/><path d="M1 3l7 6 7-6" fill="none" stroke="#141414" stroke-width="1.2"/></svg>
        youremail@xyz.com
      </p>
    </div>
  </section>

  <div class="logo-lockup">
    <div class="wordmark">
      <span class="wordmark__name">VARDENA</span>
      <span class="wordmark__line">GENERAL PAINTING LTD.</span>
    </div>
  </div>

</body>
</html>
```